Website design in Wordpress for Golf Simulator Center

We are opening a new golf simulator center in Copenhagen, and need a website design. We are using wordpress, and our site is https://vornlo-tee.dk
We will need a design for the frontpage, and a design for subpages (which we will be reusing for all subpages).
Logo is as seen on the site, and our base color scheme is leaf green.
As text, take the text on the current website, or put some placeholder text in english.
Should be responsive and look good on both desktop and mobile.
Target Market(s)
Male, 18-60, golf players

```html
<!DOCTYPE html>
<html lang="da">
<head>
<meta charset="utf-8">
<title>Vornlo Tee – sidedesign</title>
<link href="https://fonts.googleapis.com/css2?family=Teko:wght@500;600&family=Saira+Extra+Condensed:wght@400;500;600&family=Poppins:wght@400&display=swap" rel="stylesheet">
<style>
:root{
  --stage:#363636;
  --leaf:#375a2c;
  --leaf-dark:#2b4722;
  --ink:#2f4d28;
  --text:#222;
  --paper:#fff;
  --input:#eefaea;
  --bar:#0b0f0a;
  --rule:#8c9a88;
}
*{box-sizing:border-box;margin:0;padding:0}
html,body{width:1128px;height:1200px;overflow:hidden;background:var(--stage)}
.canvas{position:relative;width:1128px;height:1200px}
.page{position:absolute;top:175px;background:var(--paper);overflow:hidden}
.page--home{left:84px;width:406px;height:850px}
.page--blog{left:529px;width:515px;height:850px}
.abs{position:absolute}
.site-header{left:0;right:0;top:0;background:linear-gradient(#fdfdfd,#cdd4cb)}
.brand{display:flex;align-items:center;gap:6px;font-family:"Teko",sans-serif;font-weight:500;color:var(--ink);line-height:1}
.brand-dot{border-radius:50%;background:var(--ink)}
.socials{display:flex}
.social-dot{border-radius:50%;background:var(--leaf-dark)}
.main-nav{left:0;right:0;background:var(--leaf);display:flex;font-family:"Saira Extra Condensed",sans-serif;font-weight:600;color:#fff;letter-spacing:.6px}
.main-nav span{display:flex;align-items:center;height:100%}
.main-nav .is-active{background:var(--leaf-dark)}
.hero{left:0;right:0;background:linear-gradient(120deg,#2d4d24 0%,#4f7a3c 35%,#6a9a4c 55%,#3a5c2d 80%,#24381d 100%)}
.hero-title{font-family:"Teko",sans-serif;font-weight:600;color:#fff;font-size:16px;line-height:1}
.hero-text{font-family:"Saira Extra Condensed",sans-serif;color:#fff;font-size:8px;line-height:11px}
.btn{background:var(--leaf);color:#fff;font-family:"Saira Extra Condensed",sans-serif;font-weight:600;display:flex;align-items:center;justify-content:center;gap:4px;border-radius:3px}
.dots{display:flex;gap:8px}
.dots i{display:block;width:25px;height:3px;background:#8fa784;border-radius:2px}
.dots i.on{background:#fff}
h2,.h{font-family:"Teko",sans-serif;font-weight:600;color:var(--ink);letter-spacing:.6px;line-height:.95}
.body{font-family:"Poppins",sans-serif;color:var(--text);font-size:5.6px;line-height:8.2px}
.label{font-family:"Saira Extra Condensed",sans-serif;color:var(--text)}
.field{background:var(--input);border:1px solid #9aa894;border-radius:2px}
.rule{height:2px;background:var(--rule)}
.footer{left:0;right:0;background:var(--leaf);color:#dfe8da;font-family:"Saira Extra Condensed",sans-serif}
.footer .row{display:flex;align-items:center;gap:8px}
.bottom-bar{left:0;right:0;background:var(--bar);color:#fff;font-family:"Saira Extra Condensed",sans-serif;display:flex;align-items:center;justify-content:center}
.meta{font-family:"Saira Extra Condensed",sans-serif;color:var(--ink);display:flex;align-items:center;gap:4px}
.meta span{display:flex;align-items:center;gap:3px;margin-right:10px}
.btn-outline{border:1px solid #fff;color:#fff;border-radius:3px;display:flex;align-items:center;justify-content:center;font-family:"Saira Extra Condensed",sans-serif;font-weight:600}
</style>
</head>
<body>
<div class="canvas">

<section class="page page--home">
  <header class="abs site-header" style="height:34px">
    <div class="abs brand" style="left:46px;top:10px;font-size:15px"><i class="brand-dot" style="width:9px;height:9px"></i><span>Vornlo Tee</span></div>
    <div class="abs socials" style="left:286px;top:10px;gap:7px">
      <i class="social-dot" style="width:14px;height:14px"></i><i class="social-dot" style="width:14px;height:14px"></i><i class="social-dot" style="width:14px;height:14px"></i><i class="social-dot" style="width:14px;height:14px"></i>
    </div>
  </header>
  <nav class="abs main-nav" style="top:34px;height:20px;padding-left:39px;font-size:7.5px">
    <span class="is-active" style="padding:0 6px">HJEM</span><span style="padding:0 13px">BLOG</span><span style="padding:0 6px">FIND VEJ</span><span style="padding:0 12px">ORDBOG</span><span style="padding:0 6px">KONTAKT OS</span>
  </nav>
  <div class="abs hero" style="top:54px;height:271px" role="img" aria-label="Photo of two golfers at an indoor golf simulator screen, green tinted">
    <div class="abs hero-title" style="left:43px;top:121px">Topmoderne teknologi</div>
    <div class="abs hero-text" style="left:43px;top:137px;width:260px">Vores hightech simulatorer fra Skytrace fanger med høj præcision holden fra dit slag. Se dit data på storskærm.</div>
    <div class="abs btn" style="left:43px;top:163px;width:51px;height:17px;font-size:7px">Se mere
      <svg width="6" height="7" viewBox="0 0 6 7"><path d="M1 0.5 4.5 3.5 1 6.5" stroke="#fff" stroke-width="1.4" fill="none"/></svg></div>
    <div class="abs dots" style="left:158px;top:258px"><i></i><i class="on"></i><i></i></div>
  </div>

  <h2 class="abs" style="left:43px;top:349px;font-size:14px">Golfsimulator i Valby åbner januar 2023</h2>
  <p class="abs body" style="left:43px;top:362px;width:310px">Til januar 2023 åbner et nyt golfsimulatorcenter i Valby med 8 simulatorer af typen Skytrace 4. Vi glæder os til at kunne byde velkommen til nye og erfarne golfspillere. Hos os kan du øve alle slags slag indendørs i ly fra regn og sne, eller gå en hel 18-hullers bane på den halve tid.</p>
  <p class="abs body" style="left:43px;top:394px;width:310px">Hver simulator giver dig en helt præcis radarmåling af dit slag, så du kan øve dig præcis som du vil på en virtuel driving range, eller på en af vores mange virtuelle baner fra hele verdenen.</p>
  <h2 class="abs" style="left:43px;top:435px;font-size:14px">Åbningsreception</h2>
  <p class="abs body" style="left:43px;top:449px;width:318px">Vi holder åbningsreception d. 21. januar 2023 fra klokken 18. Mere information kommer her på siden løbende, og via vores nyhedsbrev, som du kan tilmelde her. Vi giver desuden en rabatkode til 1 times gratis spil til alle, som tilmelder sig vores nyhedsbrev før nytår, og som stadig er tilmeldt nyhedsbrevet til vores åbningsreception.</p>
  <p class="abs body" style="left:43px;top:488px;width:320px;font-size:2.4px;line-height:3px">Ved tilmelding accepterer du at modtage nyheder og tilbud fra os. Du kan altid afmelde dig igen via linket i hver mail.</p>
  <div class="abs label" style="left:43px;top:497px;width:211px;text-align:center;font-size:7px">Emailadresse</div>
  <div class="abs field" style="left:43px;top:511px;width:211px;height:14px"></div>
  <div class="abs btn" style="left:43px;top:529px;width:211px;height:14px;font-size:6.5px">Ja tak!</div>
  <h2 class="abs" style="left:43px;top:568px;font-size:14px">Køb et opstartsmedlemsskab allerede nu!</h2>
  <div class="abs label" style="left:43px;top:589px;font-size:6.5px">Til dig selv eller som gave – <u>Mere information</u></div>
  <div class="abs" style="left:43px;top:602px;width:211px;height:113px;background:linear-gradient(160deg,#1f3a18,#0d140b 60%,#2a4a1c)" role="img" aria-label="Starter membership promotion graphic with golfer and price badge"></div>
  <div class="abs label" style="left:43px;top:722px;width:211px;text-align:center;font-size:3.5px">Tilbuddet gælder kun frem til åbningsdagen</div>
  <div class="abs rule" style="left:43px;top:753px;width:320px"></div>

  <footer class="abs footer" style="top:763px;height:63px">
    <div class="abs" style="left:43px;top:8px;display:flex;flex-direction:column;gap:6px;font-size:5px">
      <div class="row"><svg width="7" height="9" viewBox="0 0 7 9"><path d="M3.5 8.5C1 5.5.5 4.3.5 3.2a3 3 0 0 1 6 0c0 1.1-.5 2.3-3 5.3z" fill="none" stroke="#fff"/><circle cx="3.5" cy="3.2" r="1" fill="#fff"/></svg><span style="line-height:5.5px">Vornlo Tee ApS<br><b>Lærkevej 14</b><br>2720 Vanløse<br>CVR: 41109872</span></div>
      <div class="row"><svg width="7" height="7" viewBox="0 0 7 7"><path d="M1 1.2 2.3.6 3.3 2.4 2.5 3.1Q3.4 4.6 4 4.5L4.7 3.8 6.4 4.8 5.8 6.1Q3 6.4 1 1.2z" fill="none" stroke="#fff" stroke-width=".8"/></svg>Tlf.: 40 12 34 56</div>
      <div class="row"><svg width="7" height="7" viewBox="0 0 7 7"><circle cx="3.5" cy="3.5" r="3" fill="none" stroke="#fff" stroke-width=".8"/><path d="M3.5 1.8v1.8l1.2.8" stroke="#fff" stroke-width=".8" fill="none"/></svg>Åbent 14:00-23:00 alle dage</div>
    </div>
    <div class="abs label" style="left:151px;top:10px;width:210px;text-align:center;font-size:7px;color:#dfe8da">Tilmeld vores nyhedsbrev!</div>
    <div class="abs" style="left:151px;top:22px;width:210px;height:14px;background:var(--input);border-radius:2px;font-family:'Saira Extra Condensed',sans-serif;font-size:5.5px;color:#333;padding:3px 4px">Emailadresse</div>
    <div class="abs btn-outline" style="left:151px;top:40px;width:210px;height:14px;font-size:6px">Ja tak!</div>
  </footer>
  <div class="abs bottom-bar" style="top:826px;height:24px;font-size:6px">Vornlo Tee ApS</div>
</section>

<section class="page page--blog">
  <header class="abs site-header" style="height:44px">
    <div class="abs brand" style="left:59px;top:13px;font-size:20px"><i class="brand-dot" style="width:12px;height:12px"></i><span>Vornlo Tee</span></div>
    <div class="abs socials" style="left:363px;top:13px;gap:8px">
      <i class="social-dot" style="width:18px;height:18px"></i><i class="social-dot" style="width:18px;height:18px"></i><i class="social-dot" style="width:18px;height:18px"></i><i class="social-dot" style="width:18px;height:18px"></i>
    </div>
  </header>
  <nav class="abs main-nav" style="top:44px;height:24px;padding-left:56px;font-size:9.5px">
    <span style="padding-right:14px">HJEM</span><span class="is-active" style="padding:0 9px">BLOG</span><span style="padding:0 11px">FIND VEJ</span><span style="padding:0 11px">ORDBOG</span><span style="padding:0 11px">KONTAKT OS</span>
  </nav>

  <h2 class="abs h" style="left:56px;top:96px;width:165px;font-size:18px">Golfsimulator i Valby åbner januar 2023</h2>
  <div class="abs meta" style="left:56px;top:130px;font-size:8px"><span><svg width="8" height="8" viewBox="0 0 8 8"><circle cx="4" cy="4" r="3.4" fill="none" stroke="#375a2c" stroke-width=".9"/><path d="M4 2v2l1.3.9" stroke="#375a2c" stroke-width=".9" fill="none"/></svg>2022-12-22</span><span><svg width="9" height="7" viewBox="0 0 9 7"><path d="M.5 1h3l.8.9h4.2v4.6H.5z" fill="none" stroke="#375a2c" stroke-width=".9"/></svg>Uncategorized</span></div>
  <div class="abs" style="left:56px;top:147px;width:165px;height:92px;background:linear-gradient(135deg,#0e1a10,#2d6a2c 55%,#4c8a3a 70%,#111 100%)" role="img" aria-label="Golfer swinging in front of a simulator screen"></div>
  <p class="abs body" style="left:56px;top:245px;width:165px;font-size:5.2px;line-height:7.8px">Det første slag på den første simulator er slået, og nu skal vi bare have bygget de andre 7 færdige. Billedet er faktisk fra andet slag, men man kan se hvordan første slag gik, hvis man kigger nederst til højre på storskærmen. Ikke helt dårligt, ganske tæt på flaget. Det man ikke ser på dette billede, er alt rodet fra håndværkerne rundt om, som er i gang med at få de resterende simulatorer bygget færdige.</p>
  <div class="abs btn" style="left:56px;top:330px;width:165px;height:22px;font-size:9px">Se mere <svg width="7" height="9" viewBox="0 0 7 9"><path d="M1 .8 5.5 4.5 1 8.2" stroke="#fff" stroke-width="1.7" fill="none"/></svg></div>

  <h2 class="abs h" style="left:295px;top:96px;width:130px;font-size:18px">Golf træning på simulator</h2>
  <div class="abs meta" style="left:295px;top:130px;font-size:8px"><span><svg width="8" height="8" viewBox="0 0 8 8"><circle cx="4" cy="4" r="3.4" fill="none" stroke="#375a2c" stroke-width=".9"/><path d="M4 2v2l1.3.9" stroke="#375a2c" stroke-width=".9" fill="none"/></svg>2022-08-04</span><span><svg width="9" height="7" viewBox="0 0 9 7"><path d="M.5 1h3l.8.9h4.2v4.6H.5z" fill="none" stroke="#375a2c" stroke-width=".9"/></svg>Uncategorized</span></div>
  <div class="abs" style="left:295px;top:147px;width:139px;height:92px;background:linear-gradient(135deg,#101820,#3a4a6a 40%,#c47a3a 55%,#2a5a2a 75%,#0c0c0c)" role="img" aria-label="Two golfers practising at a simulator with a target green on screen"></div>
  <p class="abs body" style="left:295px;top:245px;width:165px;font-size:5.2px;line-height:7.8px">Golf træning kan ske direkte på en golf simulator hos Vornlo Tee i Valby. Her får du mulighed for både at træne med en Pro, eller træne selv. Vores 8 moderne Skytrace simulatorer giver dig rig mulighed for at træne præcis den del af dit spil du har lyst til. Hvis du ofte flækker bolden på 6-jernet, har problemer med chips eller dit drive hooker helt forkert, så kan du træne det samme slag så mange gange du har brug for. Vores simulatorer måler dit slag, og du får løbende statistik over din forbedringer. Både lange og korte slag. Træningen foregår således på præcis samme måde som de professionelle golfspillere træner deres spil.</p>
  <div class="abs btn" style="left:295px;top:385px;width:164px;height:22px;font-size:9px">Se mere <svg width="7" height="9" viewBox="0 0 7 9"><path d="M1 .8 5.5 4.5 1 8.2" stroke="#fff" stroke-width="1.7" fill="none"/></svg></div>

  <h2 class="abs h" style="left:56px;top:434px;width:165px;font-size:18px">Golfudstyr til brug på en simulator</h2>
  <div class="abs meta" style="left:56px;top:472px;font-size:8px"><span><svg width="8" height="8" viewBox="0 0 8 8"><circle cx="4" cy="4" r="3.4" fill="none" stroke="#375a2c" stroke-width=".9"/><path d="M4 2v2l1.3.9" stroke="#375a2c" stroke-width=".9" fill="none"/></svg>2022-07-20</span><span><svg width="9" height="7" viewBox="0 0 9 7"><path d="M.5 1h3l.8.9h4.2v4.6H.5z" fill="none" stroke="#375a2c" stroke-width=".9"/></svg>Uncategorized</span></div>
  <div class="abs" style="left:56px;top:490px;width:139px;height:92px;background:linear-gradient(135deg,#8a8f94,#6b4a3a 45%,#3a3a3a 70%,#d8d8d8)" role="img" aria-label="Golf clubs in a bag against a patterned wall"></div>
  <p class="abs body" style="left:56px;top:587px;width:165px;font-size:5.2px;line-height:7.8px">Det golfudstyr du bruger på en simulator er det samme udstyr som du bruger på en rigtig golfbane. Køllerne og boldene er de samme, og det er stort set det eneste udstyr du får brug for, når du skal spille indendørs golf hos Vornlo Tee. Derudover kan golftøj, sko, handsker og tees være en god idé. Du vil også gerne have en golfbag til at holde alle køllerne.</p>
  <div class="abs btn" style="left:56px;top:665px;width:165px;height:22px;font-size:9px">Se mere <svg width="7" height="9" viewBox="0 0 7 9"><path d="M1 .8 5.5 4.5 1 8.2" stroke="#fff" stroke-width="1.7" fill="none"/></svg></div>

  <h2 class="abs h" style="left:295px;top:434px;width:165px;font-size:18px">Minigolf eller golfsimulator – hvad skal man vælge?</h2>
  <div class="abs meta" style="left:295px;top:490px;font-size:8px"><span><svg width="8" height="8" viewBox="0 0 8 8"><circle cx="4" cy="4" r="3.4" fill="none" stroke="#375a2c" stroke-width=".9"/><path d="M4 2v2l1.3.9" stroke="#375a2c" stroke-width=".9" fill="none"/></svg>2022-07-06</span><span><svg width="9" height="7" viewBox="0 0 9 7"><path d="M.5 1h3l.8.9h4.2v4.6H.5z" fill="none" stroke="#375a2c" stroke-width=".9"/></svg>Uncategorized</span></div>
  <div class="abs" style="left:295px;top:506px;width:139px;height:92px;background:linear-gradient(135deg,#3f7a2a,#6aa83a 50%,#2f6a22)" role="img" aria-label="Putters around a hole on artificial turf"></div>
  <p class="abs body" style="left:295px;top:603px;width:165px;font-size:5.2px;line-height:7.8px">At spille minigolf har de fleste prøvet. Her spiller man på en lille bane, som ikke er meget længere end 4-5 meter, og det gælder om at få bolden i hul på færrest slag. En af de flotteste minigolfbaner i Danmark, er Hanne's i Nordcentret, som er åbnet for nyligt. Her spiller man på kunstigt græs, og der er rigtige vandhazarder på banerne i små udgaver.</p>
  <div class="abs btn" style="left:295px;top:680px;width:164px;height:22px;font-size:9px">Se mere <svg width="7" height="9" viewBox="0 0 7 9"><path d="M1 .8 5.5 4.5 1 8.2" stroke="#fff" stroke-width="1.7" fill="none"/></svg></div>

  <div class="abs rule" style="left:55px;top:726px;width:405px"></div>

  <footer class="abs footer" style="top:738px;height:81px">
    <div class="abs" style="left:48px;top:10px;display:flex;flex-direction:column;gap:8px;font-size:6.5px">
      <div class="row"><svg width="9" height="11" viewBox="0 0 7 9"><path d="M3.5 8.5C1 5.5.5 4.3.5 3.2a3 3 0 0 1 6 0c0 1.1-.5 2.3-3 5.3z" fill="none" stroke="#fff"/><circle cx="3.5" cy="3.2" r="1" fill="#fff"/></svg><span style="line-height:7px">Vornlo Tee ApS<br><b>Lærkevej 14</b><br>2720 Vanløse<br>CVR: 41109872</span></div>
      <div class="row"><svg width="9" height="9" viewBox="0 0 7 7"><path d="M1 1.2 2.3.6 3.3 2.4 2.5 3.1Q3.4 4.6 4 4.5L4.7 3.8 6.4 4.8 5.8 6.1Q3 6.4 1 1.2z" fill="none" stroke="#fff" stroke-width=".8"/></svg>Tlf.: 40 12 34 56</div>
      <div class="row"><svg width="9" height="9" viewBox="0 0 7 7"><circle cx="3.5" cy="3.5" r="3" fill="none" stroke="#fff" stroke-width=".8"/><path d="M3.5 1.8v1.8l1.2.8" stroke="#fff" stroke-width=".8" fill="none"/></svg>Åbent 14:00-23:00 alle dage</div>
    </div>
    <div class="abs label" style="left:191px;top:12px;width:268px;text-align:center;font-size:9px;color:#dfe8da">Tilmeld vores nyhedsbrev!</div>
    <div class="abs" style="left:191px;top:27px;width:268px;height:19px;background:var(--input);border-radius:2px;font-family:'Saira Extra Condensed',sans-serif;font-size:7.5px;color:#222;padding:4px 1px">Emailadresse</div>
    <div class="abs btn-outline" style="left:191px;top:51px;width:268px;height:18px;font-size:8px">Ja tak!</div>
  </footer>
  <div class="abs bottom-bar" style="top:819px;height:31px;font-size:7.5px">Vornlo Tee ApS</div>
</section>

</div>
</body>
</html>
```